PLUME study results infographic

We enjoyed the previous infographic design you provided for us (The GLaRN cohort study Infographic), and would like to invite you to design another infographic in a similar style and layout.
We need an infographic which presents the results from the PLUME research trial. It should be colourful and engaging, in understandable language and showing the steps to get to the results. This is to showcase the results to patients/the public/clinicians, giving a brief summary of what the study proved. The final design should have the PLUME logo at the top (please see attached and https://plume.vextru.qb.zz.example/welcome-plume-trial)
I have attached the required logos which need to be used (PLUME, Carrowby Injury and Acute Care, University of Carrowby) as well as an example from another study, The GLaRN cohort study Infographic, as an example of what the layout could look like. Please DO NOT use the content from the The GLaRN cohort study Infographic example though, please instead use the content from the attached document 'PLUME_InfographicDesignInformation_PitchHive'.

```html
<!DOCTYPE html>
<html lang="en">
<head>
<meta charset="utf-8">
<title>PLUME study results infographic</title>
<link href="https://fonts.googleapis.com/css2?family=Poppins:wght@400;500;600;700;800&display=swap" rel="stylesheet">
<style>
:root{
  --navy:#22375f;
  --navy-deep:#1b2f57;
  --sky:#1ea6ea;
  --bar-dark:#4f6eae;
  --page:#f1f4fd;
  --card:#ffffff;
  --ink:#1d2331;
  --grey:#8a8f98;
  --red:#e3262f;
  --partner:#c44a4f;
}
*{box-sizing:border-box;margin:0;padding:0}
html,body{width:848px;height:1200px;overflow:hidden;background:var(--page)}
body{font-family:'Poppins',sans-serif;color:var(--ink)}
.poster{position:relative;width:848px;height:1200px;background:var(--page);overflow:hidden}
.abs{position:absolute}
.corner-line{position:absolute;left:0;top:0}

.brand{left:95px;top:88px;display:flex;align-items:center;gap:10px}
.brand-dot{width:34px;height:34px;border-radius:50%;background:var(--sky)}
.brand-name{font-size:44px;font-weight:700;color:var(--navy);letter-spacing:1px;line-height:1}

.card{position:absolute;background:var(--card);border-radius:24px}
.banner{position:absolute;background:var(--navy);color:#fff;font-weight:700;display:flex;align-items:center;line-height:1;
  clip-path:polygon(0 0,calc(100% - 22px) 0,100% 50%,calc(100% - 22px) 100%,0 100%)}
.banner.hex{justify-content:center;
  clip-path:polygon(22px 0,calc(100% - 22px) 0,100% 50%,calc(100% - 22px) 100%,22px 100%,0 50%)}
.banner.large{font-size:31px;padding-left:29px}
.banner.small{font-size:23.5px;padding-left:10px}

.illus{position:absolute;border-radius:16px}

/* Study title */
.title-banner{left:52px;top:180px;width:273px;height:56px}
.title-card{left:52px;top:208px;width:726px;height:116px}
.title-text{left:81px;top:255px;width:480px;font-size:13.6px;line-height:19.3px}
.illus-lab{left:563px;top:163px;width:215px;height:162px;background:linear-gradient(160deg,#e7f2fd,#b9dcf6 60%,#9fd2c8)}

.headline{left:0;top:338px;width:848px;text-align:center;font-size:28px;line-height:35px;font-weight:700;color:var(--navy)}

/* Summary */
.summary-banner{left:52px;top:416px;width:363px;height:55px}
.summary-card{left:52px;top:444px;width:726px;height:185px}
.summary-text{left:81px;top:481px;width:440px;font-size:13.6px;line-height:19.3px}
.illus-hospital{left:526px;top:434px;width:274px;height:196px;background:linear-gradient(180deg,#eef1f5,#c9dff3 45%,#3a8ed8 85%,#9ccc65)}

/* Key findings */
.findings-card{left:62px;top:664px;width:717px;height:141px}
.findings-banner{left:254px;top:638px;width:324px;height:55px;font-size:31px}
.finding{position:absolute;top:706px;text-align:center;font-size:9px;line-height:13.4px}
.finding b{font-weight:700}
.finding-icon{position:absolute}

/* Eligibility */
.elig-banner{left:59px;top:815px;width:250px;height:55px}
.elig-card{left:59px;top:843px;width:376px;height:100px}
.crit{position:absolute;font-size:10px;line-height:14.6px}
.crit b{font-weight:700}
.inclusion{left:97px;top:875px;width:104px}
.exclusion{left:251px;top:877px;width:176px}
.audience{left:68px;top:961px;width:215px;font-size:10px;line-height:14.6px}
.illus-care{left:318px;top:956px;width:90px;height:70px;background:linear-gradient(160deg,#f3e3cc,#4fb4e8)}

.uni{left:68px;top:1044px;width:92px;height:92px;background:var(--navy-deep);display:flex;flex-direction:column;justify-content:flex-end;padding:0 7px 10px}
.uni span{display:block;font-size:8.5px;line-height:10.5px;font-weight:500;color:#fff}

/* Study design */
.design-banner{left:450px;top:815px;width:250px;height:55px}
.design-card{left:450px;top:843px;width:339px;height:246px}
.design-line{left:488px;top:876px;width:282px;font-size:10px;line-height:14.3px}
.design-line b{font-weight:700}
.stat{position:absolute;top:915px;width:92px;text-align:center;font-size:9.2px;line-height:12.8px}
.stat b{font-weight:700}
.outcome{position:absolute;top:1002px;font-size:9.2px;line-height:13px}
.outcome b{font-weight:700}
.primary{left:458px;width:104px}
.secondary{left:598px;width:118px}
.illus-check{left:716px;top:1004px;width:65px;height:68px;background:linear-gradient(150deg,#3b4f78,#f2b53c)}

.partner{left:417px;top:1112px;display:flex;align-items:center;gap:6px}
.partner-mark{width:26px;height:26px;background:var(--partner)}
.partner-name{font-size:19.5px;font-weight:400;color:var(--grey);letter-spacing:.3px;white-space:nowrap;line-height:1}

.footer{left:26px;top:1160px;width:796px;height:40px;background:var(--navy);border-radius:24px 24px 0 0;display:flex;align-items:center;padding-left:21px;gap:9px;color:#fff;font-size:14px}
</style>
</head>
<body>
<main class="poster">

  <svg class="corner-line" width="848" height="160" viewBox="0 0 848 160"><line x1="585" y1="0" x2="848" y2="154" stroke="var(--navy)" stroke-width="3"/></svg>

  <div class="abs brand"><span class="brand-dot"></span><span class="brand-name">PLUME</span></div>

  <section>
    <div class="card title-card"></div>
    <div class="banner large title-banner">Study Title</div>
    <p class="abs title-text">A feasibility study of standard dressings versus negative-pressure wound therapy in the treatment of adult patients having surgical incisions for hip fractures: the PLUME randomized controlled trial</p>
    <div class="illus illus-lab" role="img" aria-label="Illustration of two clinicians beside a large hip X-ray screen with medical supplies"></div>
  </section>

  <h1 class="abs headline">Hip fracture surgery: can ‘vacuum’ dressings<br>reduce deep infections? (Feasibility trial)</h1>

  <section>
    <div class="card summary-card"></div>
    <div class="banner large summary-banner">Study Summary:</div>
    <p class="abs summary-text">Adults &gt;65 years undergoing hip fracture surgery at 5 UK centres were randomised to standard dressings or negative pressure ‘vacuum’ dressings (iNPWT). Deep infection (CDC-defined) was assessed at 30 &amp; 90 days; other outcomes like Health Related Quality of Life were assessed at 120 days. The overall deep SSI rate was ~4%; effect signals favored iNPWT, and a definitive trial was deemed feasible.</p>
    <div class="illus illus-hospital" role="img" aria-label="Illustration of older patients walking and in a wheelchair in front of a hospital building"></div>
  </section>

  <section>
    <div class="card findings-card"></div>
    <div class="banner hex findings-banner">Key Findings:</div>

    <div class="finding" style="left:76px;width:140px"><b>462 valid randomisations;</b><br>recruitment rate ~62% of eligible cases.</div>
    <svg class="finding-icon" style="left:123px;top:749px" width="46" height="51" viewBox="0 0 48 52" fill="var(--sky)">
      <circle cx="9" cy="7" r="6"/><circle cx="24" cy="7" r="6"/><circle cx="39" cy="7" r="6"/>
      <rect x="1" y="15" width="15" height="22" rx="4"/><rect x="32" y="15" width="15" height="22" rx="4"/>
      <rect x="15" y="15" width="18" height="24" rx="4"/>
      <rect x="4" y="34" width="4" height="17"/><rect x="9" y="34" width="4" height="17"/>
      <rect x="35" y="34" width="4" height="17"/><rect x="40" y="34" width="4" height="17"/>
      <rect x="18" y="36" width="5" height="16"/><rect x="25" y="36" width="5" height="16"/>
    </svg>

    <div class="finding" style="left:231px;width:120px"><b>Deep SSI at 30 days:</b><br>6.4% (standard) vs 1.9% (iNPWT).</div>
    <svg class="finding-icon" style="left:264px;top:748px" width="52" height="51" viewBox="0 0 56 54">
      <text x="14" y="4" font-size="2.6" fill="var(--grey)" font-family="Poppins,sans-serif">iNPWT Std</text>
      <line x1="8" y1="6" x2="8" y2="47" stroke="#ddd" stroke-width=".5"/>
      <line x1="8" y1="47" x2="54" y2="47" stroke="#ddd" stroke-width=".5"/>
      <rect x="12" y="37" width="17" height="10" fill="var(--sky)"/>
      <rect x="33" y="7" width="17" height="40" fill="var(--bar-dark)"/>
      <text x="16" y="52" font-size="2.6" fill="var(--grey)" font-family="Poppins,sans-serif">iNPWT</text>
      <text x="38" y="52" font-size="2.6" fill="var(--grey)" font-family="Poppins,sans-serif">Std</text>
    </svg>

    <div class="finding" style="left:360px;width:120px"><b>Deep SSI at 90 days:</b><br>6.4% vs 2.3%.</div>
    <svg class="finding-icon" style="left:392px;top:748px" width="52" height="51" viewBox="0 0 56 54">
      <line x1="8" y1="6" x2="8" y2="47" stroke="#ddd" stroke-width=".5"/>
      <line x1="8" y1="47" x2="54" y2="47" stroke="#ddd" stroke-width=".5"/>
      <rect x="12" y="36" width="17" height="11" fill="var(--sky)"/>
      <rect x="33" y="7" width="17" height="40" fill="var(--bar-dark)"/>
      <text x="16" y="52" font-size="2.6" fill="var(--grey)" font-family="Poppins,sans-serif">iNPWT</text>
      <text x="38" y="52" font-size="2.6" fill="var(--grey)" font-family="Poppins,sans-serif">Std</text>
    </svg>

    <div class="finding" style="left:488px;width:124px"><b>Overall 30-day deep SSI:</b><br>4.2% for hip fracture<br>population.</div>
    <svg class="finding-icon" style="left:522px;top:749px" width="56" height="52" viewBox="0 0 56 54">
      <circle cx="28" cy="27" r="20" fill="none" stroke="var(--bar-dark)" stroke-width="12"/>
      <path d="M8 27 A20 20 0 0 1 28 7 A20 20 0 0 1 47 21" fill="none" stroke="var(--sky)" stroke-width="12"/>
      <text x="0" y="3" font-size="2.6" fill="var(--grey)" font-family="Poppins,sans-serif">SSI</text>
      <text x="46" y="52" font-size="2.6" fill="var(--grey)" font-family="Poppins,sans-serif">No SSI</text>
    </svg>

    <div class="finding" style="left:627px;width:136px"><b>Feasibility confirmed for a fully powered effectiveness trial.</b></div>
    <svg class="finding-icon" style="left:674px;top:755px" width="42" height="42" viewBox="0 0 40 40">
      <circle cx="20" cy="20" r="19" fill="var(--sky)"/>
      <path d="M11 20 l6 6 l12 -12" fill="none" stroke="#fff" stroke-width="4" stroke-linecap="round" stroke-linejoin="round"/>
    </svg>
  </section>

  <section>
    <div class="card elig-card"></div>
    <div class="banner small elig-banner">Eligibility Criteria:</div>
    <svg class="abs" style="left:68px;top:893px" width="22" height="22" viewBox="0 0 20 20">
      <circle cx="10" cy="10" r="9.5" fill="var(--sky)"/>
      <path d="M5.5 10 l3 3 l6 -6" fill="none" stroke="#fff" stroke-width="2" stroke-linecap="round" stroke-linejoin="round"/>
    </svg>
    <p class="crit inclusion"><b>Inclusion:</b> Age &gt;65 years; undergoing any surgery for hip fracture.</p>
    <svg class="abs" style="left:217px;top:893px" width="22" height="22" viewBox="0 0 20 20">
      <circle cx="10" cy="10" r="8" fill="none" stroke="var(--red)" stroke-width="2.2"/>
      <line x1="4.5" y1="15.5" x2="15.5" y2="4.5" stroke="var(--red)" stroke-width="2.2"/>
    </svg>
    <p class="crit exclusion"><b>Exclusion:</b> Undisplaced intracapsular fracture treated with cannulated screws; other factors precluding participation.</p>

    <p class="abs audience">Orthopaedic &amp; trauma clinicians, orthogeriatric teams, infection prevention leads, commissioners, and patient/public audiences.</p>
    <div class="illus illus-care" role="img" aria-label="Illustration of a nurse supporting an older patient"></div>

    <div class="abs uni"><span>University of Carrowby</span></div>
  </section>

  <section>
    <div class="card design-card"></div>
    <div class="banner small design-banner">Study Design:</div>
    <svg class="abs" style="left:459px;top:874px" width="22" height="29" viewBox="0 0 20 26">
      <rect x="2" y="4" width="16" height="20" rx="2" fill="none" stroke="var(--sky)" stroke-width="1.4"/>
      <rect x="6" y="2" width="8" height="4" rx="1" fill="#fff" stroke="var(--sky)" stroke-width="1.4"/>
      <path d="M10 9 v6 M7 12 h6" stroke="var(--sky)" stroke-width="1.4"/>
      <path d="M5 19 h10 M5 21.5 h7" stroke="var(--sky)" stroke-width="1"/>
    </svg>
    <p class="abs design-line"><b>Design:</b> Two-arm multicenter RCT embedded in the GLaRN cohort.</p>

    <div class="stat" style="left:446px"><b>Sites:</b><br>5 UK centres.</div>
    <div class="stat" style="left:529px"><b>Participants:</b><br>462 randomised.</div>
    <div class="stat" style="left:623px"><b>Recruitment:</b><br>Jul 2017–Feb 2018.</div>
    <div class="stat" style="left:712px;width:72px"><b>Follow-up:</b><br>120 days.</div>

    <svg class="abs" style="left:463px;top:943px" width="53" height="44" viewBox="0 0 46 38">
      <rect x="1" y="14" width="11" height="22" fill="#fff" stroke="var(--navy)" stroke-width="1.2"/>
      <rect x="34" y="14" width="11" height="22" fill="#fff" stroke="var(--navy)" stroke-width="1.2"/>
      <rect x="12" y="3" width="22" height="33" fill="#fff" stroke="var(--navy)" stroke-width="1.2"/>
      <path d="M23 6 v10 M18 11 h10" stroke="var(--red)" stroke-width="3"/>
      <g fill="var(--sky)"><rect x="4" y="19" width="5" height="3"/><rect x="4" y="25" width="5" height="3"/><rect x="37" y="19" width="5" height="3"/><rect x="37" y="25" width="5" height="3"/><rect x="16" y="20" width="4" height="3"/><rect x="21" y="20" width="4" height="3"/><rect x="26" y="20" width="4" height="3"/><rect x="16" y="26" width="4" height="3"/><rect x="21" y="26" width="4" height="3"/><rect x="26" y="26" width="4" height="3"/></g>
    </svg>
    <svg class="abs" style="left:540px;top:945px" width="64" height="40" viewBox="0 0 54 36">
      <circle cx="12" cy="8" r="7" fill="var(--navy)"/><circle cx="42" cy="8" r="7" fill="var(--navy)"/>
      <path d="M0 30 a12 12 0 0 1 24 0z M30 30 a12 12 0 0 1 24 0z" fill="var(--navy)"/>
      <circle cx="27" cy="11" r="8" fill="var(--sky)"/>
      <path d="M12 36 a15 15 0 0 1 30 0z" fill="var(--sky)"/>
    </svg>
    <svg class="abs" style="left:653px;top:947px" width="33" height="34" viewBox="0 0 30 30">
      <rect x="1" y="4" width="28" height="25" rx="2" fill="#fff" stroke="#d8dde6"/>
      <rect x="1" y="4" width="28" height="6" fill="var(--sky)"/>
      <g fill="#c9cfd9"><rect x="4" y="13" width="3" height="3"/><rect x="9" y="13" width="3" height="3"/><rect x="14" y="13" width="3" height="3"/><rect x="19" y="13" width="3" height="3"/><rect x="24" y="13" width="3" height="3"/><rect x="4" y="18" width="3" height="3"/><rect x="9" y="18" width="3" height="3"/><rect x="14" y="18" width="3" height="3"/><rect x="19" y="18" width="3" height="3"/><rect x="24" y="18" width="3" height="3"/><rect x="4" y="23" width="3" height="3"/><rect x="9" y="23" width="3" height="3"/><rect x="14" y="23" width="3" height="3"/></g>
    </svg>
    <svg class="abs" style="left:735px;top:951px" width="30" height="30" viewBox="0 0 26 26">
      <circle cx="13" cy="13" r="11" fill="none" stroke="var(--sky)" stroke-width="1.6"/>
      <path d="M13 6 v7 h6" fill="none" stroke="var(--sky)" stroke-width="1.6" stroke-linecap="round"/>
    </svg>

    <p class="outcome primary"><b>Primary Outcome:</b><br>Deep SSI at 30 &amp; 90 days (CDC).</p>
    <svg class="abs" style="left:473px;top:1047px" width="55" height="34" viewBox="0 0 48 32">
      <path d="M4 2 v8 a9 9 0 0 0 18 0 v-8" fill="none" stroke="var(--sky)" stroke-width="1.6"/>
      <path d="M13 19 v4 a8 8 0 0 0 16 0 v-6 a6 6 0 0 1 12 0" fill="none" stroke="var(--sky)" stroke-width="1.6"/>
      <circle cx="41" cy="12" r="3.5" fill="none" stroke="var(--sky)" stroke-width="1.6"/>
    </svg>

    <p class="outcome secondary"><b>Secondary Outcomes:</b><br>Recruitment metrics, further surgery, EQ-5D-5L, complications, mobility, residential status.</p>
    <div class="illus illus-check" role="img" aria-label="Illustration of a clipboard checklist with ticks"></div>
  </section>

  <div class="abs partner"><span class="partner-mark"></span><span class="partner-name">CARROWBY INJURY &amp; ACUTE CARE</span></div>

  <footer class="abs footer">
    <svg width="30" height="18" viewBox="0 0 26 16"><rect x="1" y="1" width="24" height="14" fill="none" stroke="#fff" stroke-width="1.4"/><path d="M1 1 l12 9 l12 -9 M1 15 l9 -7 M25 15 l-9 -7" fill="none" stroke="#fff" stroke-width="1.4"/></svg>
    <span>r.halden@nacre.qb.zz.example</span>
  </footer>
</main>
</body>
</html>
```